Web design

We need the design for the logo and website for a women fashion website. No coding required. The colors used should be neutral (maybe with a light touch of color), the style should be modern, slightly luxurious, not too crowded. The target market is young professionals who love trendy clothes.
Updates

Need extra days to review

Target Market(s)

Young professionals

Industry/Entity Type

Apparel

Number of Pages Required

5+ page

Font styles to use
Sans Serif
Other font styles liked:
• Montserrat, Engravers Gothic, Benton Sans, gotham-book

Colors

Designer to choose colors to be used in the design.

```html
<!DOCTYPE html>
<html lang="en">
<head>
<meta charset="utf-8">
<title>Solenne — Women's Fashion</title>
<link href="https://fonts.googleapis.com/css2?family=Lora:ital,wght@0,400;0,500;1,400;1,500&family=Montserrat:wght@400;500;600&display=swap" rel="stylesheet">
<style>
  :root {
    --ink: #3a2f2b;
    --muted: #8a7d78;
    --rust: #b5654a;
    --sale: #d9473f;
    --blush: #f4e9e6;
    --paper: #ffffff;
    --line: #e6dcd8;
    --hero-a: #cdb8a6;
    --hero-b: #8c6a55;
  }
  * { box-sizing: border-box; margin: 0; padding: 0; }
  html, body { width: 1200px; height: 3432px; overflow: hidden; }
  body { position: relative; background: var(--paper); color: var(--ink); font-family: "Montserrat", sans-serif; }
  .serif { font-family: "Lora", serif; }
  .photo { position: absolute; }

  /* Hero */
  .hero { position: absolute; left: 0; top: 0; width: 1200px; height: 728px;
    background: linear-gradient(100deg, #9c7f6b 0%, #c8ab96 45%, #b07a63 70%, #7a5a48 100%); }
  .nav { position: absolute; left: 0; top: 0; width: 1200px; height: 110px; display: flex; align-items: center; padding: 0 72px; color: #fff; }
  .brand { display: flex; flex-direction: column; align-items: center; gap: 6px; font-family: "Lora", serif; font-size: 22px; letter-spacing: 2px; }
  .brand-dot { width: 12px; height: 12px; border-radius: 50%; background: #fff; }
  .nav-links { display: flex; gap: 40px; margin-left: 90px; font-size: 14px; }
  .nav-links .sale { color: #ff6b63; }
  .nav-tools { margin-left: auto; display: flex; gap: 30px; font-size: 14px; align-items: center; }
  .nav-tools span { display: flex; align-items: center; gap: 8px; }
  .hero-copy { position: absolute; left: 72px; top: 210px; width: 520px; color: #fff; }
  .hero-title { font-family: "Lora", serif; font-size: 66px; line-height: 1.15; font-weight: 400; }
  .hero-text { margin-top: 40px; font-size: 13px; line-height: 1.9; opacity: .92; }
  .btn { display: inline-flex; align-items: center; gap: 12px; border: 1px solid currentColor; padding: 12px 22px; font-size: 15px; }
  .hero .btn { margin-top: 52px; background: #fff; color: var(--ink); border-color: #fff; }

  /* Features */
  .features { position: absolute; left: 72px; top: 760px; width: 1056px; height: 152px; background: var(--blush); display: flex; align-items: center; padding: 0 48px; }
  .feature { flex: 1; display: flex; gap: 18px; align-items: center; }
  .feature-icon { width: 52px; height: 52px; border-radius: 50%; background: #fff; display: grid; place-items: center; flex: none; }
  .feature h3 { font-size: 15px; font-weight: 500; }
  .feature p { font-size: 12px; color: var(--muted); margin-top: 6px; width: 200px; line-height: 1.5; }

  /* Shop now */
  .section-title { position: absolute; left: 0; width: 1200px; text-align: center; font-family: "Lora", serif; font-size: 46px; font-weight: 400; color: #5a4c47; }
  .products { position: absolute; left: 76px; top: 1598px; width: 1048px; display: flex; justify-content: space-between; }
  .product { width: 248px; position: relative; }
  .product-img { width: 248px; height: 376px; }
  .tag { position: absolute; top: 0; right: 0; width: 0; height: 0; border-top: 56px solid #ff7b6b; border-left: 56px solid transparent; }
  .swatches { display: flex; gap: 6px; margin-top: 14px; }
  .swatches i { width: 18px; height: 14px; display: block; }
  .product h4 { font-family: "Lora", serif; font-weight: 400; font-size: 17px; margin-top: 12px; color: var(--rust); }
  .product .meta { font-size: 11px; color: var(--muted); margin-top: 6px; }
  .product .price { font-size: 12px; color: var(--sale); margin-top: 6px; }
  .arrow { position: absolute; top: 1765px; }

  /* Collection */
  .collection { position: absolute; left: 72px; top: 2140px; width: 1056px; height: 486px;
    background: linear-gradient(90deg, #5e6b4c 0%, #8a8a70 22%, #d8c6b8 45%, #e2d3c8 70%, #cbb6a8 100%); }
  .collection-title { position: absolute; left: 0; width: 1056px; top: 160px; text-align: center; color: #fff; font-family: "Lora", serif; font-style: italic; font-size: 78px; transform: rotate(-4deg); }
  .collection .btn { position: absolute; left: 452px; top: 300px; color: #fff; padding: 12px 30px; }

  /* Social */
  .social-sub { position: absolute; top: 2780px; left: 0; width: 1200px; text-align: center; font-size: 13px; color: var(--muted); }
  .grid { position: absolute; left: 76px; top: 2830px; width: 1048px; display: grid; grid-template-columns: repeat(4, 248px); justify-content: space-between; row-gap: 22px; }
  .grid div { height: 290px; }
</style>
</head>
<body>

<section class="hero" role="img" aria-label="Woman in a rust two-piece outfit seated on a rattan chair beside a plant">
  <nav class="nav">
    <div class="brand"><span class="brand-dot"></span>SOLENNE</div>
    <div class="nav-links"><span>Latest Arrivals</span><span>Clothes ⌄</span><span>SHOP Club</span><span class="sale">Sale</span></div>
    <div class="nav-tools">
      <span><svg width="14" height="14" viewBox="0 0 14 14" fill="none" stroke="#fff" stroke-width="1.5"><circle cx="6" cy="6" r="4.5"/><path d="M9.5 9.5L13 13"/></svg>Search</span>
      <span><svg width="16" height="14" viewBox="0 0 16 14" fill="none" stroke="#fff" stroke-width="1.4"><path d="M1 1h2l2 8h8l2-6H4"/><circle cx="6" cy="12" r="1"/><circle cx="12" cy="12" r="1"/></svg>0</span>
      <span><svg width="14" height="14" viewBox="0 0 14 14" fill="none" stroke="#fff" stroke-width="1.4"><circle cx="7" cy="4.5" r="3"/><path d="M1.5 13c1-3 3-4.5 5.5-4.5s4.5 1.5 5.5 4.5"/></svg>Login</span>
    </div>
  </nav>
  <div class="hero-copy">
    <h1 class="hero-title">Mid season Sale<br>Upto 60% off</h1>
    <p class="hero-text">Discover refined essentials for the modern woman, tailored silhouettes and soft fabrics designed to move from morning meetings to evening plans with quiet, effortless confidence.</p>
    <a class="btn">Shop Now →</a>
  </div>
</section>

<section class="features">
  <div class="feature">
    <div class="feature-icon"><svg width="24" height="24" viewBox="0 0 24 24" fill="none" stroke="#3a2f2b" stroke-width="1.3"><circle cx="12" cy="12" r="9"/><path d="M3 12h18M12 3c3 3 3 15 0 18M12 3c-3 3-3 15 0 18"/></svg></div>
    <div><h3>Worldwide Shipping</h3><p>Fast delivery to over 80 countries worldwide</p></div>
  </div>
  <div class="feature">
    <div class="feature-icon"><svg width="24" height="24" viewBox="0 0 24 24" fill="none" stroke="#3a2f2b" stroke-width="1.3"><rect x="3" y="5" width="18" height="16" rx="2"/><path d="M3 10h18M8 3v4M16 3v4"/></svg></div>
    <div><h3>30 Days Return Policy</h3><p>Easy returns within thirty days of purchase</p></div>
  </div>
  <div class="feature">
    <div class="feature-icon"><svg width="26" height="24" viewBox="0 0 26 24" fill="none" stroke="#3a2f2b" stroke-width="1.3"><path d="M2 6h13v11H2zM15 10h5l4 4v3h-9"/><circle cx="7" cy="18" r="2"/><circle cx="19" cy="18" r="2"/></svg></div>
    <div><h3>Free Shipping</h3><p>On every order above fifty dollars</p></div>
  </div>
</section>

<div class="photo" role="img" aria-label="Three women in tailored suits posing against a light grey wall" style="left:0;top:940px;width:1200px;height:520px;background:linear-gradient(90deg,#d9d6d3 0%,#c9a58e 30%,#b3694f 50%,#d3cfcb 68%,#8a5a44 85%,#dcd9d6 100%);"></div>

<h2 class="section-title" style="top:1478px;">Shop Now</h2>

<svg class="arrow" style="left:36px" width="14" height="20" viewBox="0 0 14 20" fill="none" stroke="#3a2f2b" stroke-width="1.6"><path d="M10 3L3 10l7 7"/></svg>
<svg class="arrow" style="left:1150px" width="14" height="20" viewBox="0 0 14 20" fill="none" stroke="#3a2f2b" stroke-width="1.6"><path d="M4 3l7 7-7 7"/></svg>

<section class="products">
  <article class="product">
    <div class="product-img" role="img" aria-label="Model in a corset top and light wash jeans" style="background:linear-gradient(180deg,#cfcac8,#a8adb5);"></div>
    <div class="swatches"><i style="background:#6b6b6b"></i><i style="background:#a39a7a"></i><i style="background:#3d4a3a"></i><i style="background:#222"></i><i style="background:#c9b29a"></i><i style="background:#7a3f34"></i></div>
    <h4>Sylvia</h4><p class="meta">Cotton blend, regular fit</p><p class="price">$49.00</p>
  </article>
  <article class="product">
    <div class="product-img" role="img" aria-label="Model in a rust knit mini dress" style="background:linear-gradient(180deg,#d1cbc8,#a2573f 55%,#c7c1be);"></div>
    <div class="swatches"><i style="background:#6b6b6b"></i><i style="background:#a39a7a"></i><i style="background:#3d4a3a"></i><i style="background:#222"></i><i style="background:#c9b29a"></i><i style="background:#7a3f34"></i></div>
    <h4>Tulip</h4><p class="meta">Cotton blend, regular fit</p><p class="price">$49.00</p>
  </article>
  <article class="product">
    <div class="product-img" role="img" aria-label="Model in a white fitted midi dress" style="background:linear-gradient(180deg,#cdc8c5,#ece7e1 55%,#c8c3c0);"></div>
    <div class="swatches"><i style="background:#6b6b6b"></i><i style="background:#a39a7a"></i><i style="background:#3d4a3a"></i><i style="background:#222"></i><i style="background:#c9b29a"></i><i style="background:#7a3f34"></i></div>
    <h4>Monique</h4><p class="meta">Cotton blend, regular fit</p><p class="price">$49.00</p>
  </article>
  <article class="product">
    <div class="product-img" role="img" aria-label="Model in a brown blazer dress" style="background:linear-gradient(180deg,#cfcac7,#8b4a35 55%,#c9c4c1);"></div>
    <span class="tag"></span>
    <div class="swatches"><i style="background:#6b6b6b"></i><i style="background:#a39a7a"></i><i style="background:#3d4a3a"></i><i style="background:#222"></i><i style="background:#c9b29a"></i><i style="background:#7a3f34"></i></div>
    <h4>Sylvia</h4><p class="meta">Cotton blend, regular fit</p><p class="price">$49.00</p>
  </article>
</section>

<section class="collection" role="img" aria-label="Woman in a pink belted dress beside palm leaves">
  <div class="collection-title">Shop by Collection</div>
  <a class="btn">Shop Now</a>
</section>

<h2 class="section-title" style="top:2700px;">#Solenne</h2>
<p class="social-sub">Share your styled looks on our social page, mention us @solenne #solenne</p>

<section class="grid">
  <div role="img" aria-label="Woman in a pink ruffled outfit on a terrace" style="background:linear-gradient(180deg,#d9cfc6,#e6a9b0);"></div>
  <div role="img" aria-label="Woman in a black top and trousers" style="background:linear-gradient(180deg,#ece8e4,#2c2a2a);"></div>
  <div role="img" aria-label="Couple dressed up on a city street" style="background:linear-gradient(180deg,#8a8c90,#3d5572);"></div>
  <div role="img" aria-label="Woman in a white dress in a garden" style="background:linear-gradient(180deg,#9bb08a,#eee8e3);"></div>
  <div role="img" aria-label="Woman in a white tailored coat" style="background:linear-gradient(180deg,#e5e0da,#f4f2ef);"></div>
  <div role="img" aria-label="Woman seated by a pool on a sunny day" style="background:linear-gradient(180deg,#9fc2de,#e7e3dc);"></div>
  <div role="img" aria-label="Woman in a light summer dress on the beach" style="background:linear-gradient(180deg,#c9a47f,#d8c8b6);"></div>
  <div role="img" aria-label="Woman in a white outfit posing outdoors" style="background:linear-gradient(180deg,#d9d3cb,#f1ede8);"></div>
</section>

</body>
</html>
```